Awesome photographers card for an awesome new business

Double sided business card Black background and silver logo in middle on one side. Details on otherside. please keep it simple

Photographer

Gavin Tolley
0482615073
GavinTolleyPhotography82@lumenpost.com
www.GavinTolleyPhotography.com.au
Instagram _Gavin_tolley

Requirements
Must have
• My logo in Silver
• please use instagram logo instead of "Instagram"

```html
<!DOCTYPE html>
<html lang="en">
<head>
<meta charset="utf-8">
<title>Gavin Tolley Photography – Business Card</title>
<link rel="stylesheet" href="https://fonts.googleapis.com/css2?family=Roboto+Condensed:wght@400&display=swap">
<style>
  :root {
    --backdrop: #3b332d;
    --card-top: #56575a;
    --card-bottom: #050505;
    --silver: #d6d6d6;
    --silver-soft: #c9c9c9;
  }
  * { margin: 0; padding: 0; box-sizing: border-box; }
  html, body {
    width: 1200px;
    height: 1000px;
    overflow: hidden;
    background: var(--backdrop);
    font-family: "Roboto Condensed", "Arial Narrow", sans-serif;
  }
  .card {
    position: absolute;
    left: 235px;
    width: 788px;
    height: 450px;
    overflow: hidden;
    background: linear-gradient(to bottom, var(--card-top), var(--card-bottom));
  }
  .card--front { top: 20px; }
  .card--back { top: 527px; }

  .brand {
    position: absolute;
    display: flex;
    align-items: center;
    color: var(--silver);
    font-weight: 400;
    text-transform: uppercase;
  }
  .brand__ring {
    flex: none;
    border: 3px solid var(--silver);
    border-radius: 50%;
  }
  .brand__name { line-height: 1.15; }

  .card--front .brand {
    left: 50%;
    top: 50%;
    transform: translate(-50%, -50%);
    gap: 28px;
    font-size: 38px;
    letter-spacing: 6px;
  }
  .card--front .brand__ring { width: 90px; height: 90px; }

  .card--back .brand {
    left: 62px;
    top: 150px;
    gap: 14px;
    font-size: 20px;
    letter-spacing: 3px;
  }
  .card--back .brand__ring { width: 46px; height: 46px; border-width: 2px; }

  .details {
    position: absolute;
    left: 342px;
    top: 68px;
    width: 420px;
    color: var(--silver);
  }
  .details__name {
    font-size: 50px;
    font-weight: 400;
    letter-spacing: 1.5px;
    line-height: 1;
  }
  .details__rule {
    width: 117px;
    height: 2px;
    background: var(--silver-soft);
    margin: 30px 0 34px;
    border: 0;
  }
  .details__list { list-style: none; }
  .details__list li {
    font-size: 22px;
    letter-spacing: 0.6px;
    line-height: 44.5px;
    white-space: nowrap;
    color: var(--silver-soft);
  }
</style>
</head>
<body>
  <section class="card card--front" aria-label="Card front">
    <div class="brand">
      <span class="brand__ring" aria-hidden="true"></span>
      <span class="brand__name">Gavin Tolley<br>Photography</span>
    </div>
  </section>

  <section class="card card--back" aria-label="Card back">
    <div class="brand">
      <span class="brand__ring" aria-hidden="true"></span>
      <span class="brand__name">Gavin Tolley<br>Photography</span>
    </div>
    <div class="details">
      <h1 class="details__name">Gavin Tolley</h1>
      <hr class="details__rule">
      <ul class="details__list">
        <li>0482615073</li>
        <li>GavinTolleyPhotography82@lumenpost.com</li>
        <li>www.GavinTolleyPhotography.com.au</li>
        <li>_Gavin_tolley</li>
      </ul>
    </div>
  </section>
</body>
</html>
```